Post Card Design Bright Lantern Youth

We need a postcard design that will be mailed to all residents offering free pickups of donated clothing. Our foundation is called Bright Lantern Youth, we are a nonprofit charitable organization that provides meals and medical services to children in need in Honduras. Collecting unwanted second-hand clothing generates revenue that helps fund the mission and programs run by our foundation. We would like to offer our pickup services to everyone who has any unwanted reusable clothing.

```html
<!DOCTYPE html>
<html lang="en">
<head>
<meta charset="utf-8">
<title>Bright Lantern Youth – Clothing Donation Postcard</title>
<link rel="stylesheet" href="https://fonts.googleapis.com/css2?family=Passion+One:wght@400;700&family=Noto+Serif:wght@400&display=swap">
<style>
  :root {
    --backdrop: #a5a4a0;
    --card: #ffffff;
    --yellow: #ffcc07;
    --pink: #e6068f;
    --blue: #0893d9;
    --green: #7dc243;
    --ink: #1d1d1b;
    --rule: #555555;
    --field: #e6e6e6;
    --box-line: #7a7a7a;
  }
  * { box-sizing: border-box; margin: 0; padding: 0; }
  html, body { width: 1200px; height: 1200px; overflow: hidden; }
  body { background: var(--backdrop); position: relative; }

  .postcard {
    position: absolute;
    left: 220px;
    width: 763px;
    height: 545px;
    background: var(--card);
    overflow: hidden;
  }
  .postcard--front { top: 47px; }
  .postcard--back { top: 609px; height: 544px; }

  .org-name {
    position: absolute;
    font-family: "Passion One", sans-serif;
    font-weight: 700;
    color: var(--green);
    text-align: center;
    line-height: 1;
    white-space: nowrap;
    display: flex;
    flex-direction: column;
    align-items: center;
  }
  .org-name__dot {
    border-radius: 50%;
    background: var(--green);
  }
  .postcard--front .org-name { left: 22px; top: 34px; width: 190px; font-size: 30px; gap: 12px; }
  .postcard--front .org-name__dot { width: 60px; height: 60px; }
  .postcard--back .org-name { left: 22px; top: 16px; width: 160px; font-size: 24px; gap: 8px; }
  .postcard--back .org-name__dot { width: 50px; height: 50px; }

  .headline-band {
    position: absolute; top: 0; right: 0;
    width: 550px; height: 175px;
  }
  .headline {
    font-family: "Passion One", sans-serif;
    font-weight: 700;
    text-transform: uppercase;
    line-height: 1;
  }
  .pink { color: var(--pink); }
  .blue { color: var(--blue); }

  .postcard--front .headline {
    position: absolute; left: 273px; top: 62px;
    font-size: 45px; line-height: 44px; letter-spacing: 0.3px;
  }

  .donation-art {
    position: absolute; left: 130px; top: 190px;
    width: 520px; height: 355px;
    background: radial-gradient(ellipse at 45% 60%, #c79a6e 0%, #d8b48c 40%, #f3e6d6 75%, #ffffff 100%);
  }

  .postcard--back .headline {
    position: absolute; left: 25px; top: 148px;
    font-size: 43px; line-height: 43.5px;
  }
  .mission {
    position: absolute; left: 28px; top: 298px; width: 318px;
    font-family: "Noto Serif", serif;
    font-size: 12.4px; line-height: 15px; color: var(--ink);
  }
  .mission p + p { margin-top: 15px; }

  .leaf-corner {
    position: absolute; left: 0; top: 397px;
    width: 208px; height: 147px;
    background: linear-gradient(135deg, rgba(230,6,143,0.25) 0%, rgba(255,204,7,0.3) 45%, rgba(8,147,217,0.25) 75%, rgba(125,194,67,0.2) 100%);
  }

  .divider {
    position: absolute; left: 381px; top: 100px;
    width: 1px; height: 366px; background: var(--rule);
  }

  .stamp-box { position: absolute; left: 643px; top: 44px; width: 72px; height: 97px; }

  .postcode {
    position: absolute; left: 413px; top: 206px;
    display: flex; gap: 3px;
  }
  .postcode span {
    width: 20.5px; height: 27px;
    border: 1.5px solid var(--box-line);
  }

  .address-lines {
    position: absolute; left: 413px; top: 260px; width: 301px;
    display: flex; flex-direction: column; gap: 8.5px;
  }
  .address-lines span { height: 34px; background: var(--field); }
</style>
</head>
<body>

<section class="postcard postcard--front">
  <div class="org-name"><span class="org-name__dot"></span><span>Bright Lantern<br>Youth</span></div>
  <svg class="headline-band" viewBox="0 0 550 175" aria-hidden="true">
    <polygon points="59,0 550,0 550,175 0,175" fill="var(--yellow)"/>
  </svg>
  <h1 class="headline">
    <span class="pink">Donate</span> <span class="blue">your clothes</span><br>
    <span class="pink">to save lives</span>
  </h1>
  <div class="donation-art" role="img" aria-label="Illustration of a cardboard donation box overflowing with clothes, bags, hats and shoes, with colourful leaves behind it"></div>
</section>

<section class="postcard postcard--back">
  <div class="org-name"><span class="org-name__dot"></span><span>Bright Lantern<br>Youth</span></div>
  <h2 class="headline">
    <span class="pink">Donate</span><br>
    <span class="blue">your clothes</span><br>
    <span class="pink">to save lives</span>
  </h2>
  <div class="mission">
    <p>We provides meals and medical services to children in need in Honduras.</p>
    <p>Collecting unwanted second-hand clothing generates revenue that helps fund the mission and programs run by our foundation.</p>
  </div>
  <div class="leaf-corner" role="img" aria-label="Decorative cluster of colourful leaves on a green stem"></div>

  <div class="divider"></div>

  <svg class="stamp-box" viewBox="0 0 72 97" aria-hidden="true">
    <rect x="1.5" y="1.5" width="69" height="94" fill="#ffffff" stroke="#9a9a9a" stroke-width="1.5" stroke-dasharray="3 2.5"/>
    <polygon points="70,48 70,95 28,95" fill="#eeeeee"/>
  </svg>

  <div class="postcode" aria-hidden="true">
    <span></span><span></span><span></span><span></span><span></span>
    <span></span><span></span><span></span><span></span><span></span>
  </div>

  <div class="address-lines" aria-hidden="true">
    <span></span><span></span><span></span><span></span><span></span>
  </div>
</section>

</body>
</html>
```